Town Planning Consultants require lstationary design

Require a design to be used for our letterhead and report cover page. We have an approved logo.
we have attached our logo, and our temporary letterhead/cover page (SEE Cover) which we currently adapt for both purposes in the interim pending a permanent design. I have also attached an example (example report cover) of a report cover page that I like. perhaps similar with our colour scheme

Target Market(s)

?

Industry/Entity Type

Town

Colors
249fd4
3176b5

Requirements
Must have
• colours to match logo
• the text content in existing letterhead

```html
<!DOCTYPE html>
<html lang="en">
<head>
<meta charset="utf-8">
<title>Statement of Environmental Effects – Report Cover</title>
<link rel="stylesheet" href="https://fonts.googleapis.com/css2?family=Roboto+Condensed:wght@400;700&family=Jost:wght@400;600&family=Questrial&display=swap">
<style>
  :root {
    --brand-light: #249fd4;
    --brand-dark: #3176b5;
    --panel: #2a76b5;
    --box-top: #29a2d8;
    --box-bottom: #05a0da;
    --ink: #222;
    --white: #fff;
  }
  * { margin: 0; padding: 0; box-sizing: border-box; }
  html, body { width: 848px; height: 1200px; overflow: hidden; background: var(--white); }
  .cover { position: relative; width: 848px; height: 1200px; }

  .brand {
    position: absolute; left: 92px; top: 78px;
    display: flex; align-items: center; gap: 14px;
    font-family: "Questrial", sans-serif; font-size: 62px; color: var(--brand-light);
    letter-spacing: -1px; line-height: 1;
  }
  .brand-square { width: 26px; height: 26px; background: var(--brand-light); }

  .header-rule { position: absolute; left: 421px; top: 33px; width: 2px; height: 124px; background: var(--brand-dark); }

  .contact {
    position: absolute; left: 472px; top: 56px;
    font-family: "Roboto Condensed", sans-serif; font-size: 17px; line-height: 21.5px; color: var(--ink);
    list-style: none;
  }

  .panels { position: absolute; left: 0; top: 0; }

  .title-box, .subject-box {
    position: absolute; border-radius: 17px; color: var(--white); text-align: center;
    background: linear-gradient(to bottom, var(--box-top), var(--box-bottom));
  }
  .title-box { left: 75px; top: 429px; width: 714px; height: 132px; display: flex; align-items: center; justify-content: center; }
  .title {
    font-family: "Roboto Condensed", sans-serif; font-weight: 700; font-size: 37px; letter-spacing: 0.3px;
  }
  .subject-box { left: 79px; top: 592px; width: 716px; height: 218px; }
  .subject { font-family: "Jost", sans-serif; font-weight: 600; font-size: 27px; margin-top: 61px; letter-spacing: 0.6px; }
  .site { font-family: "Jost", sans-serif; font-weight: 400; font-size: 19.5px; margin-top: 12px; letter-spacing: 0.3px; }

  .credits {
    position: absolute; right: 66px; top: 853px; list-style: none; text-align: right;
    font-family: "Roboto Condensed", sans-serif; font-weight: 700; font-size: 21px; line-height: 32.6px; color: var(--white);
  }

  .footer-rule { position: absolute; left: 37px; top: 1143px; width: 787px; height: 3px; background: var(--brand-light); }
  .services {
    position: absolute; top: 1164px; left: 0; width: 848px; list-style: none;
    font-family: "Jost", sans-serif; font-size: 16px; color: var(--brand-light);
  }
  .services li { position: absolute; white-space: nowrap; }
</style>
</head>
<body>
<main class="cover">
  <div class="brand"><span class="brand-square"></span><span class="brand-name">Tallowood</span></div>
  <div class="header-rule"></div>
  <ul class="contact">
    <li>A: 17 Harbour Ridge Road, MARLOWE NSW 2479</li>
    <li>T:&nbsp; +61 (2) 5550 1234</li>
    <li>M: +61 (0) 400 555 018</li>
    <li>E: hello@tallowood.com.au</li>
  </ul>

  <svg class="panels" width="848" height="1200" viewBox="0 0 848 1200" aria-hidden="true">
    <path fill="var(--panel)" d="M58 320 L406 261 Q416 259 416 270 L414 994 L58 961 Q38 959 38 940 L38 343 Q38 324 58 320 Z"/>
    <path fill="var(--panel)" d="M448 341 L806 374 Q824 376 824 396 L824 990 Q824 1008 806 1012 L452 1075 Q445 1076 445 1068 Z"/>
  </svg>

  <section class="title-box"><h1 class="title">STATEMENT OF ENVIROMENTAL EFFECTS</h1></section>
  <section class="subject-box">
    <h2 class="subject">Proposed Additions to Existing Dwelling</h2>
    <p class="site">12 Wattle Crescent, ASHGROVE</p>
  </section>

  <ul class="credits">
    <li>Prepared for: R. Ellison</li>
    <li>Prepared by: M. Hartley</li>
    <li>Reviewed by: D. Carrow</li>
    <li>Dated: June, 2016</li>
  </ul>

  <div class="footer-rule"></div>
  <ul class="services">
    <li style="left:69px">PLANNING</li>
    <li style="left:252px">DEVELOPMENT</li>
    <li style="left:479px">URBAN DESIGN</li>
    <li style="left:685px">CONSULTANTS</li>
  </ul>
</main>
</body>
</html>
```